Starfold Pemba, need to create new label for organic, probiotic TONIC drinks collection.

we need an exciting new label for our new line of probiotic drinks.

TONICS:
Ginger and lime
Turmeric and black pepper
Tamarind and cardamon
Our product is an organic, locally sourced fermented probiotic beverage that helps people to improve digestive health and overall immunity. We would like to rebrand our currently existing EMBER SPRITZ as part of a broader range of TONICS (other flavours mentioned above). We would like to start with the GINGER AND LIME and progress from that design to render the other flavours. We like the use of ginger and lime motif, we also like an energetic, bright, minimal style. we want the label to communicate the ENERGY of living things and an ACTIVE lifestyle. Find our current label below

Target Market(s)

Young adults as well as adults. Both men and women middle to upper class within East African market

Industry/Entity Type

Functional beveragess

Colors

Designer to choose colors to be used in the design.

Requirements
Must have
• all information from previous label included. please build a colour pallet on based on the colour of the drink itself. Images in attachments
Nice to have
• minimal, active, playful, youthful, energetic
Should not have
• too much detail or should not be too busy

```html
<!DOCTYPE html>
<html lang="en">
<head>
<meta charset="utf-8">
<title>Starfold Pemba – Ember Spritz label, front and back</title>
<link rel="stylesheet" href="https://fonts.googleapis.com/css2?family=Titan+One&family=Quicksand:wght@500;600;700&family=Poppins:wght@800&display=swap">
<style>
  :root {
    --canvas: #ffffff;
    --frame: #fdd3dc;
    --cream: #faf7ec;
    --coral: #f37c70;
    --coral-pill: #ef6f6a;
    --ink: #1d1d1d;
    --body: #2b2b2b;
    --lime: #bcd67a;
    --lime-rim: #7ea352;
    --ginger: #e8b38a;
    --sugar-icon: #ecb98c;
    --badge: #7ea352;
  }
  * { box-sizing: border-box; margin: 0; padding: 0; }
  html, body { width: 1200px; height: 1200px; overflow: hidden; background: var(--canvas); }
  body { position: relative; font-family: "Quicksand", sans-serif; color: var(--body); }

  .label {
    position: absolute; top: 70px; width: 470px; height: 740px;
    background: var(--frame); border-radius: 235px / 230px; padding: 20px;
  }
  .label--front { left: 75px; }
  .label--back { left: 655px; }
  .label__face {
    width: 100%; height: 100%; background: var(--cream);
    border-radius: 215px / 210px; position: relative; text-align: center;
  }

  .brand { display: flex; align-items: center; justify-content: center; gap: 10px; }
  .brand__dot { width: 18px; height: 18px; border-radius: 50%; background: var(--ink); }
  .brand__name { font-family: "Quicksand", sans-serif; font-weight: 700; color: var(--ink); }

  .label--front .brand { padding-top: 80px; }
  .label--front .brand__name { font-size: 38px; }
  .product-title {
    font-family: "Titan One", sans-serif; color: var(--coral);
    font-size: 70px; line-height: 0.98; margin-top: 22px; letter-spacing: 1px;
  }
  .hero-art {
    position: relative; width: 310px; height: 230px; margin: 20px auto 0;
  }
  .hero-art__fill {
    width: 100%; height: 100%; border-radius: 46% 54% 50% 50%;
    background: linear-gradient(110deg, var(--lime) 0%, var(--lime) 42%, var(--ginger) 62%, var(--ginger) 100%);
  }
  .vegan-badge {
    position: absolute; right: -6px; bottom: 4px; width: 64px; height: 64px;
    border-radius: 50%; border: 3px solid var(--badge); background: var(--cream);
  }
  .flavour {
    font-weight: 700; color: var(--coral); font-size: 30px; letter-spacing: 1px; margin-top: 22px;
  }
  .volume {
    display: inline-block; margin-top: 12px; background: var(--coral-pill); color: #fff;
    font-weight: 700; font-size: 21px; letter-spacing: 1px; padding: 6px 24px; border-radius: 24px;
  }

  .label--back .label__face { padding: 56px 46px 0; }
  .section-title { font-weight: 700; color: var(--coral); font-size: 19px; letter-spacing: 0.5px; }
  .copy { font-size: 14px; line-height: 1.42; font-weight: 500; margin-top: 8px; }
  .section { margin-top: 18px; }
  .facts { display: flex; align-items: flex-start; gap: 10px; margin-top: 18px; text-align: left; }
  .sugar-icon {
    flex: none; width: 62px; height: 62px; border-radius: 50%;
    border: 4px solid var(--sugar-icon); margin-top: 6px; position: relative; overflow: hidden;
  }
  .sugar-icon::after {
    content: ""; position: absolute; left: -4px; top: 27px; width: 70px; height: 4px;
    background: var(--sugar-icon); transform: rotate(-45deg);
  }
  .facts__sugar { width: 128px; }
  .facts__sugar .section-title { font-size: 17px; }
  .facts__sugar .copy { margin-top: 4px; font-size: 13px; line-height: 1.35; }
  .facts__dates { font-size: 13px; }
  .date-label { font-weight: 700; color: var(--coral); font-size: 9.5px; letter-spacing: 0.3px; margin-top: 2px; }
  .date-value { font-weight: 500; margin-top: 3px; margin-bottom: 14px; }
  .care { font-weight: 700; color: var(--coral); font-size: 20px; line-height: 1.3; letter-spacing: 0.5px; margin-top: 20px; }
  .footer { display: flex; justify-content: center; align-items: center; gap: 26px; margin-top: 20px; }
  .footer .brand__name { font-size: 20px; }
  .footer .brand__dot { width: 11px; height: 11px; }
  .social { text-align: left; font-size: 11.5px; font-weight: 500; }
  .social .section-title { font-size: 12px; margin-bottom: 4px; }
  .social__row { display: flex; align-items: center; gap: 5px; margin-top: 3px; }
  .social__mark { width: 8px; height: 8px; border-radius: 50%; background: var(--coral); }

  .caption {
    position: absolute; top: 860px; width: 470px; text-align: center;
    font-family: "Poppins", sans-serif; font-weight: 800; font-size: 38px; color: #000; letter-spacing: 1px;
  }
  .caption--front { left: 75px; }
  .caption--back { left: 655px; }
</style>
</head>
<body>

<section class="label label--front" aria-label="Front label">
  <div class="label__face">
    <div class="brand"><span class="brand__dot"></span><span class="brand__name">Starfold</span></div>
    <h1 class="product-title">EMBER<br>SPRITZ</h1>
    <div class="hero-art">
      <div class="hero-art__fill" role="img" aria-label="Illustration of a lime slice and a ginger root with small scattered dots"></div>
      <div class="vegan-badge" aria-hidden="true"></div>
    </div>
    <p class="flavour">GINGER &amp; LIME</p>
    <span class="volume">300 ML</span>
  </div>
</section>

<section class="label label--back" aria-label="Back label">
  <div class="label__face">
    <h2 class="section-title">EMBER SPRITZ</h2>
    <p class="copy">A fizzy &amp; sweet natural soda. More commonly known as 'ginger beer', this non alcoholic beverage is full of live probiotic cultures. A fantastic remedy for inflammation, easing menstrual cramps &amp; cleansing the body of toxic chemicals.</p>

    <div class="section">
      <h2 class="section-title">INGREDIENTS</h2>
      <p class="copy">Organic ginger, Organic Lime &amp;<br>Purified water</p>
    </div>

    <div class="facts">
      <div class="sugar-icon" aria-hidden="true"></div>
      <div class="facts__sugar">
        <h2 class="section-title">NO SUGAR</h2>
        <p class="copy">This beverage contains live cultures that support your digestive health</p>
      </div>
      <div class="facts__dates">
        <p class="date-label">MANUFACTURE DATE:</p>
        <p class="date-value">01/01/2023</p>
        <p class="date-label">BEST BEFORE:</p>
        <p class="date-value">01/01/2023</p>
      </div>
    </div>

    <p class="care">SHAKE BEFORE OPENING<br>KEEP REFRIGERATED</p>

    <div class="footer">
      <div class="brand"><span class="brand__dot"></span><span class="brand__name">Starfold</span></div>
      <div class="social">
        <h2 class="section-title">FOLLOW US:</h2>
        <p class="social__row"><span class="social__mark"></span>starfoldpemba</p>
        <p class="social__row"><span class="social__mark"></span>@starfoldpemba</p>
      </div>
    </div>
  </div>
</section>

<p class="caption caption--front">FRONT</p>
<p class="caption caption--back">BACK</p>

</body>
</html>
```